poster for a contemporary music concert series

Our association is hosting a series of contemporary music concerts.
The setup is classical - from chamber music trio, midsized ensemble until orchestra.
context/topic:
Every ensemble for contemporary music in the city is playing one concert in the series. We have one common topic each year. This year’s topic is about a composition idea  called "Tonverwebung". Each concert has one assigned student who is responsible to write a new piece that will be performed. This piece uses material generated by the LAST concert of the series. The used material can be anything (the score, the recording, a video recording, ...).
task:
We need a poster that will be printed in A3 format throughout the city before every concert. The poster must contain all the information of the concert series and must have places for the individual names of the performing ensemble/title/program.
The poster is used six times for six different ensembles. Although it is ONE series, we would like to have it easily visible that there are different concerts. We think the easiest way is to use complete different colors for background to distinguish the different ensembles/program titels from each other.
Things to be included on the poster:
- the title of the concert series is "de:turns".
- the concert place is "Lindenhof-Halle Dresden, großer Saal"
- the price is  "15€ normal / 10€ ermäßigt"
- the logo of TonGeflecht-Dresden can be used in any of the colours provided - somewhere should be mentioned, that this concert series is a cooperation "de:turns – Eine Konzertreihe von TonGeflecht-Dresden in Kooperation mit dem Lindenhof-Halle Dresden"
- the logo of the museum where we play is included and should be used
- the pdf shows examples of previous years
- there must be one bottom line in white for the needed logos of the funding partners. The funding partners are different from each concert, I included here three of them for visual purposes

Updates
- please don't use parts of the old posters. We have complete new posters for every year. The rectangle and the "Intelligenz" was part of last year's design.
- the music that is coming is not classical in a way that any instrument pictures would help to promote it. It's composed today, so very modern and often with use of electronics (de:turns is often inspired composers to a  kind of feedback, loop, variance, or ... of the previous material)

Target Market(s)
concert audience, young people
Industry/Entity Type
contemporary (classical) music
Requirements
Must have
- things mentioned in the brief description

Nice to have
- a visual look that shows that it is about contemporary music. IF there is any idea how to visualize the IDEA of the concert series this year (taking material from previous concerts and recompose it to the next ensemble) - this would be WONDERFUL. not necessary a copy, nor fake - just a reference to the old ones - and so on :-)

Should not have
- symbolic images/clipart/anything "musically" --> more avantgarde or abstract style is better

```html
<!DOCTYPE html>
<html lang="de">
<head>
<meta charset="utf-8">
<title>de:turns – Konzertreihe</title>
<link rel="stylesheet" href="https://fonts.googleapis.com/css2?family=Anton&family=Nunito:wght@400;700;800;900&display=swap">
<style>
  :root{
    --page:#e9e8e5;
    --teal-light:#0aa6c4;
    --teal-mid:#0a6f82;
    --teal-dark:#053c49;
    --truss:#5f8c90;
    --truss-edge:#2f5558;
    --spot:#1d2a2e;
    --yellow:#f2c531;
    --white:#ffffff;
    --band:#ffffff;
    --ink:#444444;
    --red:#e3202a;
    --green:#2e9a47;
    --lime:#9fc85a;
    --city:#333333;
  }
  *{margin:0;padding:0;box-sizing:border-box}
  html,body{width:1200px;height:2740px;overflow:hidden;background:var(--page)}
  body{font-family:"Nunito",sans-serif;position:relative}

  .poster{
    position:absolute;left:80px;top:556px;width:1040px;height:1628px;overflow:hidden;
    background:radial-gradient(ellipse 60% 55% at 50% 52%,var(--teal-light) 0%,var(--teal-mid) 45%,var(--teal-dark) 100%);
    box-shadow:0 18px 40px rgba(0,0,0,.35);
  }

  .truss{position:absolute;left:0;top:0;width:100%;height:38px;background:var(--truss);border-bottom:3px solid var(--truss-edge)}
  .spot{position:absolute;top:52px;width:70px;height:90px;background:var(--spot);border-radius:10px}
  .spot--left{left:4px}
  .spot--right{right:4px}

  .brand{position:absolute;top:150px;left:0;width:100%;text-align:center;color:var(--yellow);font-weight:800;font-size:22px;letter-spacing:1px}
  .brand .dot{display:inline-block;width:22px;height:22px;border-radius:50%;background:var(--yellow);vertical-align:-3px;margin-right:10px}

  .title{position:absolute;top:212px;left:0;width:100%;text-align:center;font-family:"Anton",sans-serif;font-weight:400;font-size:172px;line-height:1;color:var(--white);letter-spacing:6px}
  .title .prefix{color:var(--yellow)}

  .subtitle{position:absolute;top:398px;left:0;width:100%;text-align:center;color:var(--white);font-weight:800;font-size:20px;line-height:1.3}
  .venue{position:absolute;top:470px;left:0;width:100%;text-align:center;color:var(--white);font-weight:900;font-size:33px}

  .prices{position:absolute;top:540px;left:0;width:100%;display:flex;justify-content:center;align-items:center;gap:26px;color:var(--white)}
  .price{font-weight:900;font-size:33px;line-height:1}
  .price b{display:block;color:var(--yellow);font-size:48px;font-weight:900}
  .price--normal{text-align:right}
  .price--reduced{text-align:left}
  .price-label{width:60px;padding:18px 0;font-weight:800;font-size:14px;text-align:center;line-height:1.1;
    background:linear-gradient(var(--white),var(--white)) center top/2px 14px no-repeat,
               linear-gradient(var(--white),var(--white)) center bottom/2px 14px no-repeat}

  .url{position:absolute;top:643px;left:318px;width:405px;height:40px;border:2.5px solid var(--white);color:var(--white);font-weight:800;font-size:21px;letter-spacing:3px;text-align:center;line-height:35px}

  .lineup{position:absolute;top:712px;left:0;width:100%;list-style:none;display:flex;justify-content:space-between;padding:0 175px 0 185px;color:var(--white);text-align:center;font-size:23px;line-height:1.05}
  .lineup .first{font-weight:400}
  .lineup .last{font-weight:900;text-transform:uppercase}

  .artwork{position:absolute;left:250px;top:795px;width:470px;height:520px;border-radius:40px;
    background:linear-gradient(160deg,rgba(255,255,255,.5),rgba(255,255,255,.18))}

  .bottom-band{position:absolute;left:0;bottom:0;width:100%;height:288px;background:var(--band)}

  .partners{position:absolute;left:0;top:1455px;width:100%;height:130px;display:flex;align-items:center;justify-content:space-between;padding:0 80px 0 85px}
  .partner-foundation{display:flex;gap:18px;align-items:flex-start}
  .badge--wide{width:92px;height:62px;border-radius:4px;background:var(--lime)}
  .badge--small{width:38px;height:62px;border-radius:0 0 18px 18px;background:var(--green)}
  .fineprint{font-size:7px;color:var(--ink);width:160px;line-height:1.25;margin-top:6px}
  .partner-city{display:flex;align-items:center;gap:14px}
  .partner-city .note{font-size:11px;color:var(--ink);text-align:right;line-height:1.25}
  .badge--city{width:80px;height:54px;background:var(--city);border-radius:3px}
  .venue-mark{display:flex;align-items:center;gap:8px;color:var(--red);font-weight:900;font-size:19px;line-height:1.05;text-transform:uppercase}
  .venue-mark .dot{width:38px;height:38px;border-radius:50%;background:var(--red)}
</style>
</head>
<body>
  <main class="poster">
    <div class="truss" role="img" aria-label="Stage lighting truss"></div>
    <div class="spot spot--left" role="img" aria-label="Stage spotlight"></div>
    <div class="spot spot--right" role="img" aria-label="Stage spotlight"></div>

    <div class="brand"><span class="dot"></span>TonGeflecht Dresden</div>

    <h1 class="title"><span class="prefix">DE:</span>TURNS</h1>

    <p class="subtitle">Eine Konzertreihe von TonGeflecht-Dresden in Kooperation mit dem<br>Lindenhof-Halle Dresden</p>

    <p class="venue">LINDENHOF-HALLE DRESDEN, GROßER SAAL</p>

    <div class="prices">
      <div class="price price--normal"><b>15€</b>normal</div>
      <div class="price-label">TICKET<br>PRICE</div>
      <div class="price price--reduced"><b>10€</b>ermäßigt</div>
    </div>

    <div class="url">www.tongeflecht-dresden.de</div>

    <ul class="lineup">
      <li><span class="first">LENE</span><br><span class="last">Vogt</span></li>
      <li><span class="first">TIMO</span><br><span class="last">Kessler</span></li>
      <li><span class="first">INES</span><br><span class="last">Moreau</span></li>
      <li><span class="first">PAUL</span><br><span class="last">Brandt</span></li>
      <li><span class="first">RAFA</span><br><span class="last">Lenz</span></li>
    </ul>

    <div class="artwork" role="img" aria-label="Large musical note built from many small white notes, over a faint city skyline"></div>

    <div class="bottom-band"></div>

    <div class="partners">
      <div class="partner-foundation">
        <div>
          <div class="badge--wide"></div>
          <p class="fineprint">Gefördert durch eine Landesstiftung für Kultur. Diese Maßnahme wird mitfinanziert durch Steuermittel auf Grundlage des beschlossenen Haushaltes.</p>
        </div>
        <div class="badge--small"></div>
      </div>
      <div class="partner-city">
        <p class="note">gefördert durch<br>das Amt für<br>Stadtkultur</p>
        <div class="badge--city"></div>
      </div>
      <div class="venue-mark"><span class="dot"></span><span>Lindenhof-Halle<br>Dresden</span></div>
    </div>
  </main>
</body>
</html>
```